Travel Company is looking for a STAND OUT Business Card

I need a unique Business Card that will truly stand out. Nothing too busy. Simple is good, right? Not looking for a standard design either. No cookie cutter layout. We are a Travel Company that works more with Companies than Travelers. I had an idea to focus and emphasis on the 2 logo a bit more. This is not necessary, however thought it would look interesting. I am just looking for something interesting and a bit different. Does't have to completely off the wall crazy, just not your run of the mill business card.

Target Market(s)

Hoteliers, Resort Management, Call Centers, Executives, Travelers, Families, Businesses

Industry/Entity Type

Hospitality

Contact Information for Business Card

President/CEO - Marcus T Bellamy (title not necessary if design doesn't allow for it)
contact - (407) 555-0186
email - mbellamy@wayfarenow.example
address - 4812 Quillmore Ave #164
Orlando, FL 32804
website - www.wayfarenow.example

Font styles to use
Serif
Other font styles liked:
• Avenir Next LT Pro BOLD

Requirements
Must have
• simple look and design. Unique design
Nice to have
• I attached the 2 logo separate from the main logo. This can be used separately from the Main Logo, together with the main logo or as main logo. I included the logo font. Use it or not, designers choice.
Should not have
• cookie cutter design. Little use of red other than the logo

```html
<!DOCTYPE html>
<html lang="en">
<head>
<meta charset="utf-8">
<title>Wayfare Now — Business Card</title>
<link rel="stylesheet" href="https://fonts.googleapis.com/css2?family=Open+Sans:wght@400;600;800&display=swap">
<style>
  :root {
    --page-bg: #e9e6e1;
    --card-black: #0b0b0b;
    --card-white: #ffffff;
    --brand-red: #e8151b;
    --ink-dark: #111111;
    --ink-light: #ffffff;
    --card-shadow: rgba(0, 0, 0, 0.18);
  }
  * { box-sizing: border-box; margin: 0; padding: 0; }
  html, body {
    width: 1200px;
    height: 900px;
    overflow: hidden;
    background: var(--page-bg);
    font-family: "Open Sans", Arial, sans-serif;
  }
  .canvas {
    position: relative;
    width: 1200px;
    height: 900px;
  }
  .card {
    position: absolute;
    left: 250px;
    width: 700px;
    height: 400px;
    overflow: hidden;
    box-shadow: 0 10px 28px var(--card-shadow);
  }
  .card--front { top: 40px; background: var(--card-black); }
  .card--back { top: 460px; background: var(--card-white); }

  .wordmark {
    display: flex;
    align-items: center;
    justify-content: center;
    gap: 16px;
    font-weight: 800;
    letter-spacing: -1px;
    line-height: 1;
  }
  .wordmark__dot {
    width: 30px;
    height: 30px;
    border-radius: 50%;
    background: var(--brand-red);
    flex: none;
  }
  .card--front .wordmark {
    position: absolute;
    inset: 0;
    font-size: 64px;
    color: var(--ink-light);
  }

  .back__band {
    position: absolute;
    inset: 0;
    width: 700px;
    height: 400px;
  }
  .card--back .wordmark {
    position: absolute;
    left: 0;
    right: 0;
    top: 62px;
    font-size: 58px;
    color: var(--ink-dark);
  }
  .contact {
    position: absolute;
    right: 26px;
    top: 200px;
    list-style: none;
    text-align: right;
    color: var(--ink-light);
    font-size: 15px;
    line-height: 22px;
  }
  .contact li {
    display: flex;
    align-items: center;
    justify-content: flex-end;
    gap: 6px;
  }
  .contact svg { width: 11px; height: 11px; fill: var(--ink-light); flex: none; }
  .holder {
    position: absolute;
    left: 40px;
    bottom: 34px;
    color: var(--ink-light);
  }
  .holder__name { font-size: 22px; font-weight: 600; line-height: 28px; }
  .holder__title { font-size: 17px; line-height: 22px; margin-left: 14px; margin-bottom: 14px; }
  .holder__address { font-size: 18px; line-height: 24px; margin-left: 28px; font-style: normal; }
</style>
</head>
<body>
<main class="canvas">

  <section class="card card--front" aria-label="Card front">
    <div class="wordmark"><span class="wordmark__dot"></span><span>Wayfare Now</span></div>
  </section>

  <section class="card card--back" aria-label="Card back">
    <svg class="back__band" viewBox="0 0 700 400" aria-hidden="true">
      <polygon points="0,230 700,172 700,400 0,400" fill="var(--card-black)"/>
    </svg>

    <div class="wordmark"><span class="wordmark__dot"></span><span>Wayfare Now</span></div>

    <ul class="contact">
      <li>(407) 555-0186
        <svg viewBox="0 0 12 12"><path d="M2.5 1h2l1 2.6-1.3 1a6 6 0 0 0 3.2 3.2l1-1.3L11 7.5v2c0 .8-.7 1.5-1.5 1.5A8.5 8.5 0 0 1 1 2.5C1 1.7 1.7 1 2.5 1z"/></svg>
      </li>
      <li>mbellamy@wayfarenow.example
        <svg viewBox="0 0 12 12"><path d="M1 2.5h10v7H1z M1.6 3 6 6.4 10.4 3" fill="none" stroke="#fff" stroke-width="1.2"/></svg>
      </li>
      <li>www.wayfarenow.example
        <svg viewBox="0 0 12 12"><circle cx="6" cy="6" r="5" fill="none" stroke="#fff" stroke-width="1.2"/><path d="M1 6h10M6 1c-2.4 2.8-2.4 7.2 0 10M6 1c2.4 2.8 2.4 7.2 0 10" fill="none" stroke="#fff" stroke-width="1"/></svg>
      </li>
    </ul>

    <div class="holder">
      <p class="holder__name">Marcus T Bellamy</p>
      <p class="holder__title">President/CEO</p>
      <address class="holder__address">4812 Quillmore Ave #164<br>Orlando, FL 32804</address>
    </div>
  </section>

</main>
</body>
</html>
```